Roofing Company needs YOU to help put us on top!

Brightpeak Roofing, a fresh new company with quality and Innovation in mind, needs your help to stand out in the competitive Chicago market. With over 30 years of experience, all the right people and tools for the job, the only thing we are missing is your creative ideas in web design to help us grow our online presence.
Our Company offers exceptional quality at reasonable prices, we work for the everyday people both blue collar and white collar.

We have used Craftswarm in the past with multiple successful campaigns, we are excited to see what you can come up with for our website.

www.BrightpeakRoofing.example will be the domain

We will be hiring a photographer for visual content on our pages later. Stock photos are okay to use but should follow theme.

Thank you for taking the time on the submissions, if you have any questions don't hesitate to ask and we will provide whatever is needed to you.

Target Market(s)

Homeowners & Commercial Clients between 21-65

Industry/Entity Type

Roofing

Coding

Coded - Design and coding required

Number of Pages Required

4 page

Font styles to use
Sans Serif

Colors
ffffff
ec1f27
000000
5c5c5c
757575
b2b2b2

Requirements
Must have
• Color Scheme - should follow around our logo
• As for pages we were looking for an About, Services, Projects (gallery page) and Contact.
• Main page please include social media links and a a place so people could use tillbee to make payments
• Website should work on desktop as well as mobile platforms
Nice to have
• A Live chat feature would be nice if possible
Should not have
• Obscure Colors or Common web templates

```html
<!DOCTYPE html>
<html lang="en">
<head>
<meta charset="utf-8">
<title>Brightpeak Roofing</title>
<link href="https://fonts.googleapis.com/css2?family=Oswald:wght@400;500&family=Roboto:wght@300;400;500;700&display=swap" rel="stylesheet">
<style>
:root{
  --red:#ec1f27;
  --black:#000;
  --ink:#1c1c1c;
  --dark:#23262b;
  --darker:#1a1c20;
  --grey:#5c5c5c;
  --mid:#757575;
  --light:#b2b2b2;
  --line:#cfcfcf;
  --white:#fff;
}
*{box-sizing:border-box;margin:0;padding:0}
html,body{width:1200px;height:3797px;overflow:hidden}
body{font-family:'Roboto',sans-serif;color:var(--ink);background:var(--white);position:relative}
section,header,footer{position:absolute;left:0;width:1200px}
.abs{position:absolute}
.title{position:absolute;left:0;width:1200px;text-align:center;font-size:31px;font-weight:400;letter-spacing:1px;text-transform:uppercase}
.title::after{content:"";display:block;width:46px;height:3px;background:var(--red);margin:12px auto 0}

/* header */
.site-header{top:0;height:134px;background:var(--white)}
.brand{position:absolute;left:30px;top:22px;display:flex;align-items:flex-start;gap:10px}
.brand-mark{width:22px;height:22px;background:var(--red);margin-top:6px}
.brand-name{font-family:'Roboto',sans-serif;font-weight:700;font-size:30px;line-height:1;color:var(--black);text-transform:uppercase;width:190px}
.brand-phone{position:absolute;left:62px;top:96px;font-weight:700;font-size:17px;color:var(--black)}
.nav{position:absolute;top:68px;left:380px;display:flex;align-items:center;font-size:18px;color:#333;letter-spacing:.5px}
.nav a{color:inherit;text-decoration:none;margin-right:38px}
.nav .active{background:var(--red);color:var(--white);padding:8px 28px;transform:skewX(-18deg);margin-right:36px}
.nav .active span{display:inline-block;transform:skewX(18deg)}

/* hero */
.hero{top:134px;height:500px;background:linear-gradient(120deg,#3b2a22 0%,#221a16 45%,#2c2622 100%);overflow:hidden}
.hero-photo{position:absolute;right:0;top:0;width:380px;height:500px;background:linear-gradient(180deg,#cfd6e0,#6f89b3 60%,#3b4f73)}
.hero-text{position:absolute;left:130px;width:560px;text-align:center;color:var(--white);font-family:'Oswald',sans-serif}
.hero h1{font-size:118px;font-weight:400;line-height:1;margin-top:82px}
.hero .sub{font-size:56px;line-height:1;margin-top:14px}
.hero .tag{font-size:38px;line-height:1;margin-top:38px}
.btn{display:inline-block;background:var(--red);color:var(--white);font-family:'Roboto',sans-serif;font-size:14px;padding:10px 32px;transform:skewX(-18deg);margin-top:34px;text-transform:uppercase}
.btn span{display:inline-block;transform:skewX(18deg)}

/* roofing types */
.types{top:634px;height:602px}
.types .title{top:40px}
.types .lead{position:absolute;top:115px;width:1200px;text-align:center;font-size:16px;color:#333}
.type-card{position:absolute;top:206px;width:360px;height:346px;border:1px solid #999;text-align:center}
.diamond{position:absolute;left:78px;top:-48px;width:204px;height:204px}
.type-card h3{position:absolute;top:182px;width:100%;font-weight:400;font-size:23px;letter-spacing:1px}
.type-card h3::after{content:"";display:block;width:34px;height:2px;background:var(--red);margin:10px auto 0}
.type-card p{position:absolute;top:238px;left:28px;right:28px;font-size:13.5px;line-height:1.55;color:#333}

/* services */
.services{top:1236px;height:208px;background:linear-gradient(180deg,#2c2f35,#1f2226)}
.services .title{top:42px;color:var(--white)}
.services .title::after{display:none}
.tabs{position:absolute;top:127px;left:45px;display:flex;gap:20px}
.tab{font-size:13px;color:var(--white);border:1px solid #cfcfcf;padding:8px 20px;transform:skewX(-18deg);white-space:nowrap}
.tab span{display:inline-block;transform:skewX(18deg)}
.tab.on{background:var(--red);border-color:var(--red)}
.gallery{top:1444px;height:500px}
.g-tile{position:absolute;top:0;height:500px}
.g-feature{left:101px;width:499px;background:var(--red);color:var(--white);text-align:center}
.g-feature h4{font-weight:400;font-size:29px;margin-top:172px}
.g-feature svg{margin-top:30px}

/* about */
.about{top:1944px;height:524px}
.about .title{top:44px}
.about .kicker{position:absolute;left:30px;top:114px;font-size:18px;font-weight:500}
.about .welcome{position:absolute;left:30px;top:146px;font-size:29px;line-height:1.05;color:var(--mid);text-transform:uppercase}
.about .welcome b{color:var(--red);font-weight:500}
.about .copy{position:absolute;left:30px;top:276px;width:560px;font-size:14.5px;line-height:1.65;color:var(--grey)}
.about .copy p+p{margin-top:10px}
.feature{position:absolute;left:683px;width:291px;height:86px;border:1px solid #999;border-right:none;display:flex;align-items:center;padding-left:30px;gap:28px;font-size:16px;color:var(--grey);text-transform:uppercase;letter-spacing:1px}
.about-photo{position:absolute;left:972px;top:119px;width:198px;height:354px;background:linear-gradient(160deg,#d67b44,#c9a27b 50%,#8b6b4e)}

/* news */
.news{top:2468px;height:468px;background:var(--red)}
.news .title{top:50px;color:var(--white)}
.news .title::after{background:var(--white)}
.news-card{position:absolute;top:117px;width:360px;height:260px}
.news-dark{background:#2a2a2c;color:var(--white);padding:0 24px}
.meta{display:flex;gap:10px;font-size:12px}
.meta .cat{background:var(--red);color:var(--white);padding:4px 10px}
.meta .date{color:var(--white);padding:4px 0}
.meta .com{background:var(--red);color:var(--white);padding:4px 10px}
.news-dark .meta{margin-top:44px}
.news-dark h5{font-size:18px;font-weight:500;margin-top:40px}
.news-dark p{font-size:14px;line-height:1.5;margin-top:18px}
.news-dark .more{font-size:13px;color:var(--red);margin-top:8px;display:block}
.news-img{width:360px;height:262px}
.news-card .meta.on-img{position:absolute;left:24px;bottom:0}
.on-img .cat{background:var(--white);color:var(--ink)}
.on-img .date{background:var(--white);color:var(--ink);padding:4px 8px}
.on-img .com{background:var(--white);color:var(--ink)}
.news-cap{position:absolute;left:0;top:296px;color:var(--white);font-size:18px}

/* testimonials */
.testimonials{top:2936px;height:355px}
.testimonials .title{top:48px}
.testimonials .title::after{display:none}
.quote{position:absolute;left:148px;top:130px;width:904px;text-align:center;font-size:15px;line-height:1.55;color:var(--grey)}
.qmark{position:absolute;font-family:Georgia,serif;font-size:90px;color:#ddd;line-height:1}
.avatar{position:absolute;left:490px;top:211px;width:96px;height:96px;border-radius:50%;background:linear-gradient(180deg,#c9b7ae,#3a2d2a);border:3px solid #eee}
.client{position:absolute;left:597px;top:246px;color:var(--red);font-size:20px}

/* contact */
.contact{top:3291px;height:384px;background:linear-gradient(180deg,#2a2d32,#16181b)}
.contact .title{top:48px;color:var(--white)}
.contact .title::after{display:none}
.region{position:absolute;top:132px;height:252px;color:var(--white)}
.region.map{background:rgba(255,255,255,.04)}
.region.info{background:rgba(0,0,0,.35)}
.region h6{position:absolute;left:30px;top:24px;font-size:22px;font-weight:700}
.region .pin-big{position:absolute;left:115px;top:128px}
.info-row{position:absolute;left:18px;display:flex;gap:14px;font-size:14.5px;line-height:1.5}

/* footer */
.footer-nav{top:3675px;height:52px;background:#0f1012;display:flex;justify-content:center;align-items:center;gap:18px;font-size:14px;color:#bbb}
.footer-nav .on{color:var(--red)}
.footer-base{top:3727px;height:70px;background:#0f1012;border-top:1px solid #2a2a2a}
.copyright{position:absolute;left:30px;top:26px;font-size:12px;color:#aaa}
.social{position:absolute;right:30px;top:24px;display:flex;gap:28px}
.social span{width:16px;height:16px;border-radius:50%;background:#8a8a8a;display:block}
</style>
</head>
<body>

<header class="site-header">
  <div class="brand">
    <span class="brand-mark"></span>
    <span class="brand-name">Brightpeak Roofing</span>
  </div>
  <div class="brand-phone">555-014-0100</div>
  <nav class="nav">
    <a class="active"><span>HOME</span></a>
    <a>FEATURES</a><a>ABOUT</a><a>PROJECTS</a><a>SERVICES</a><a>BLOG</a><a>CONTACT</a>
  </nav>
</header>

<section class="hero">
  <div class="hero-photo" role="img" aria-label="Smiling roofing contractor in a white hard hat with arms crossed"></div>
  <div class="hero-text">
    <h1>We Provide</h1>
    <div class="sub">Best Roofing solution for you</div>
    <div class="tag">Experties you can trust</div>
    <div class="btn"><span>More Details</span></div>
  </div>
</section>

<section class="types">
  <h2 class="title">We Provide Roofing</h2>
  <p class="lead">To many clients like Residential, Commercial and Industrial</p>

  <div class="type-card" style="left:30px">
    <svg class="diamond" viewBox="0 0 204 204" role="img" aria-label="Modern residential home at dusk"><defs><linearGradient id="g1" x1="0" y1="0" x2="0" y2="1"><stop offset="0" stop-color="#3d5f9a"/><stop offset="1" stop-color="#2a2a35"/></linearGradient></defs><polygon points="102,2 202,102 102,202 2,102" fill="#fff" stroke="#ec1f27" stroke-width="4"/><polygon points="102,16 188,102 102,188 16,102" fill="url(#g1)"/></svg>
    <h3>RESIDENTIAL</h3>
    <p>Lorem ipsum dolor sit amet consectetur adipising elittiam nisi sapienemper id turpis eget ultries imperdiet dolor. Pellentesque id volutpat</p>
  </div>
  <div class="type-card" style="left:420px">
    <svg class="diamond" viewBox="0 0 204 204" role="img" aria-label="Columned commercial building"><defs><linearGradient id="g2" x1="0" y1="0" x2="0" y2="1"><stop offset="0" stop-color="#a9c2db"/><stop offset="1" stop-color="#5b7a4a"/></linearGradient></defs><polygon points="102,2 202,102 102,202 2,102" fill="#fff" stroke="#444" stroke-width="2"/><polygon points="102,16 188,102 102,188 16,102" fill="url(#g2)"/></svg>
    <h3>COMMERCIAL</h3>
    <p>Pellentesque tempoc leo dui feugiat ero vestib ulum varius nisl risus non miellentesque et diam nisluspendisse potentiusce consectetur con</p>
  </div>
  <div class="type-card" style="left:810px">
    <svg class="diamond" viewBox="0 0 204 204" role="img" aria-label="City skyscrapers at night"><defs><linearGradient id="g3" x1="0" y1="0" x2="0" y2="1"><stop offset="0" stop-color="#1b3f7a"/><stop offset="1" stop-color="#0b1530"/></linearGradient></defs><polygon points="102,2 202,102 102,202 2,102" fill="#fff" stroke="#444" stroke-width="2"/><polygon points="102,16 188,102 102,188 16,102" fill="url(#g3)"/></svg>
    <h3>INDUSTRIAL</h3>
    <p>Aliquam luctus tellus vel pellentesque tempor leo dui feugiat eros vestibulum varius nisl risus non mellentesque et diam niuspendisse pote urna</p>
  </div>
</section>

<section class="services">
  <h2 class="title">We Offering&nbsp; Services</h2>
  <div class="tabs">
    <div class="tab on"><span>ALL SERVICES</span></div>
    <div class="tab"><span>SHINGLE ROOFS</span></div>
    <div class="tab"><span>ROOF REPAIRS</span></div>
    <div class="tab"><span>STORM DAMAGE</span></div>
    <div class="tab"><span>SHINGLE ROOFS</span></div>
    <div class="tab"><span>INSURANCE WORK</span></div>
    <div class="tab"><span>GUTTERS</span></div>
  </div>
</section>

<section class="gallery">
  <div class="g-tile" style="left:0;width:101px;background:linear-gradient(180deg,#e0a040,#8a5a2a)" role="img" aria-label="Street lamp against a warm building wall"></div>
  <div class="g-tile g-feature" role="img" aria-label="Brick house behind a red overlay">
    <h4>ROOF REPAIRS</h4>
    <svg width="46" height="46" viewBox="0 0 46 46"><circle cx="19" cy="19" r="13" fill="none" stroke="#fff" stroke-width="5"/><line x1="29" y1="29" x2="42" y2="42" stroke="#fff" stroke-width="6" stroke-linecap="round"/></svg>
  </div>
  <div class="g-tile" style="left:600px;width:499px;background:linear-gradient(180deg,#bcd3ea 0%,#8a5f4a 45%,#5b7a3c 100%)" role="img" aria-label="Two-storey brick house with dark shingle roof"></div>
  <div class="g-tile" style="left:1099px;width:101px;background:linear-gradient(180deg,#6fa3d8,#d8c98f)" role="img" aria-label="Yellow house with blue sky"></div>
</section>

<section class="about">
  <h2 class="title">About Us</h2>
  <div class="kicker">WE GREATLY APPRECIATE YOUR BUSINESS!</div>
  <h3 class="welcome">Welcome to <b>Brightpeak Roofing</b><br>when it comes to your home,<br>think Brightpeak</h3>
  <div class="copy">
    <p>First of all, thank you for choosing our company.</p>
    <p>Let us start off by telling you about our company so you have a better understanding of who we are and how we operate and why you are making the right &nbsp; decision in hiring our company. We are a family owned, owner operated company as well as a Full-Time Professional Roofing Company. &nbsp;We have built our success by providing homeowners as well as smal businesses in the entire Chicagoland and Greater Indiana area with quality work at competitive rates and providing the service you should expect from a quality roofing co.</p>
  </div>
  <div class="feature" style="top:2098px;top:154px">
    <svg width="40" height="40" viewBox="0 0 40 40" fill="none" stroke="#444" stroke-width="2"><rect x="7" y="4" width="24" height="30"/><line x1="12" y1="12" x2="26" y2="12"/><line x1="12" y1="18" x2="26" y2="18"/><circle cx="28" cy="30" r="6" fill="#fff"/></svg>LICENSED
  </div>
  <div class="feature" style="top:256px">
    <svg width="40" height="40" viewBox="0 0 40 40" fill="none" stroke="#444" stroke-width="2"><path d="M4 22 L12 14 L20 18 L28 12 L36 20"/><path d="M10 24 L18 30 L26 24"/><circle cx="20" cy="7" r="3"/></svg>BONDED
  </div>
  <div class="feature" style="top:357px">
    <svg width="40" height="40" viewBox="0 0 40 40" fill="none" stroke="#444" stroke-width="2"><path d="M20 10 C14 2 4 8 20 22 C36 8 26 2 20 10Z"/><path d="M4 26 L12 34 L20 30 L28 34 L36 26"/></svg>INSURED
  </div>
  <div class="about-photo" role="img" aria-label="Roofer in an orange hard hat laying roof panels"></div>
</section>

<section class="news">
  <h2 class="title">Latest News</h2>
  <div class="news-card news-dark" style="left:30px">
    <div class="meta"><span class="cat">Roofing</span><span class="date">● Oct 05,2016</span><span class="com">Comments 08</span></div>
    <h5>How Your House Looks</h5>
    <p>Nunc volutpat facilisis eleifend. Quisque porta, elit quis congue facilisis, quam metus mollis ipsum.</p>
    <span class="more">Read More</span>
  </div>
  <div class="news-card" style="left:420px">
    <div class="news-img" role="img" aria-label="City skyline at dusk" style="background:linear-gradient(180deg,#6f95c4,#2f3d55 70%,#1c2333)"></div>
    <div class="meta on-img"><span class="cat">Roofing</span><span class="date">Oct 05,2016</span><span class="com">Comments 08</span></div>
    <div class="news-cap">How Your House Looks</div>
  </div>
  <div class="news-card" style="left:810px">
    <div class="news-img" role="img" aria-label="Model house held in an open hand" style="background:linear-gradient(180deg,#e8eef3,#c7a58f 55%,#6aa04a)"></div>
    <div class="meta on-img"><span class="cat">Roofing</span><span class="date">Oct 05,2016</span><span class="com">Comments 08</span></div>
    <div class="news-cap">How Your House Looks</div>
  </div>
</section>

<section class="testimonials">
  <h2 class="title">Testimonilas</h2>
  <span class="qmark" style="left:100px;top:120px">&ldquo;</span>
  <p class="quote">Lorem Suspendisse ac eleifend risus. Praesent vel erat quis dui ullamcorper rhoncus id et enim. Nulla femtum necsit lorem eget Turpis metus, quis lorem ipsu consectetur adipiscing elit. Fusce sollicitudin turpis metus, quis consequat nibh elementum site. Donec varius ultrices luctus. Duis blandit vulputate erat at cursus.</p>
  <span class="qmark" style="left:1050px;top:168px">&rdquo;</span>
  <div class="avatar" role="img" aria-label="Client portrait"></div>
  <div class="client">Client Name Here</div>
</section>

<section class="contact">
  <h2 class="title">Contact Us</h2>
  <div class="region map" style="left:30px;width:275px"><h6>ILLINOIS</h6>
    <svg class="pin-big" width="50" height="58" viewBox="0 0 50 58"><path d="M25 4 C14 4 7 12 7 22 C7 34 25 50 25 50 C25 50 43 34 43 22 C43 12 36 4 25 4Z" fill="none" stroke="#ec1f27" stroke-width="4"/><circle cx="25" cy="22" r="6" fill="none" stroke="#ec1f27" stroke-width="4"/><ellipse cx="25" cy="54" rx="14" ry="3" fill="none" stroke="#ec1f27" stroke-width="2"/></svg>
  </div>
  <div class="region info" style="left:305px;width:295px">
    <div class="info-row" style="top:20px"><svg width="16" height="20" viewBox="0 0 16 20"><path d="M8 1 C4 1 1 4 1 8 C1 13 8 19 8 19 C8 19 15 13 15 8 C15 4 12 1 8 1Z" fill="none" stroke="#ec1f27" stroke-width="2"/><circle cx="8" cy="8" r="2.5" fill="#ec1f27"/></svg><span>Lorem ipsum dolor sit the<br>conse ctetur adip 012345<br>Nullam,malesuada.</span></div>
    <div class="info-row" style="top:132px"><svg width="18" height="18" viewBox="0 0 18 18"><path d="M3 2 L7 2 L8 6 L6 8 C7 10 8 11 10 12 L12 10 L16 11 L16 15 C9 16 2 9 3 2Z" fill="none" stroke="#ec1f27" stroke-width="1.8"/></svg><span>555-014-0100</span></div>
    <div class="info-row" style="top:200px"><svg width="18" height="14" viewBox="0 0 18 14"><rect x="1" y="1" width="16" height="12" fill="none" stroke="#ec1f27" stroke-width="1.8"/><path d="M1 1 L9 8 L17 1" fill="none" stroke="#ec1f27" stroke-width="1.8"/></svg><span>info@brightpeakroofing.example</span></div>
  </div>
  <div class="region map" style="left:600px;width:275px"><h6>INDIANA</h6>
    <svg class="pin-big" width="50" height="58" viewBox="0 0 50 58"><path d="M25 4 C14 4 7 12 7 22 C7 34 25 50 25 50 C25 50 43 34 43 22 C43 12 36 4 25 4Z" fill="none" stroke="#ec1f27" stroke-width="4"/><circle cx="25" cy="22" r="6" fill="none" stroke="#ec1f27" stroke-width="4"/><ellipse cx="25" cy="54" rx="14" ry="3" fill="none" stroke="#ec1f27" stroke-width="2"/></svg>
  </div>
  <div class="region info" style="left:875px;width:295px">
    <div class="info-row" style="top:20px"><svg width="16" height="20" viewBox="0 0 16 20"><path d="M8 1 C4 1 1 4 1 8 C1 13 8 19 8 19 C8 19 15 13 15 8 C15 4 12 1 8 1Z" fill="none" stroke="#ec1f27" stroke-width="2"/><circle cx="8" cy="8" r="2.5" fill="#ec1f27"/></svg><span>Lorem ipsum dolor sit the<br>conse ctetur adip 012345<br>Nullam,malesuada.</span></div>
    <div class="info-row" style="top:132px"><svg width="18" height="18" viewBox="0 0 18 18"><path d="M3 2 L7 2 L8 6 L6 8 C7 10 8 11 10 12 L12 10 L16 11 L16 15 C9 16 2 9 3 2Z" fill="none" stroke="#ec1f27" stroke-width="1.8"/></svg><span>555-014-0200</span></div>
    <div class="info-row" style="top:200px"><svg width="18" height="14" viewBox="0 0 18 14"><rect x="1" y="1" width="16" height="12" fill="none" stroke="#ec1f27" stroke-width="1.8"/><path d="M1 1 L9 8 L17 1" fill="none" stroke="#ec1f27" stroke-width="1.8"/></svg><span>info@brightpeakroofing.example</span></div>
  </div>
</section>

<footer class="footer-nav">
  <span class="on">Home</span><span>/</span><span>Features</span><span>/</span><span>About</span><span>/</span><span>Projects</span><span>/</span><span>Services</span><span>/</span><span>Blog</span><span>/</span><span>Contact us</span>
</footer>
<footer class="footer-base">
  <div class="copyright">Copyright ©Brightpeak Roofing &amp; Construction Company, Inc 2016 All rights reserved.</div>
  <div class="social" aria-label="Social media links"><span></span><span></span><span></span><span></span><span></span></div>
</footer>

</body>
</html>
```